Corvane Photography Business Card Design

I need a business card designed for a photography business based in Perth, Western Australia called Corvane Photography.

We specialise in wedding, event photography and portrait photography.

The business card must borrow the style of the attached logo.

The hex codes for the colours in the logo are:
#ED1D85 - Pink
#89C23E - Green
#37282F - Black

The name on the card will be:
Name: Teodric
Phone: 0417360825
Website: www.corvanephotography-example.com.au
Facebook: corvanephotography

I am open and happy to accept creative concepts.

Industry/Entity Type

Business

```html
<!DOCTYPE html>
<html lang="en">
<head>
<meta charset="utf-8">
<title>Teodric – Corvane Photography Business Card</title>
<link rel="stylesheet" href="https://fonts.googleapis.com/css2?family=Work+Sans:wght@300;400&display=swap">
<style>
  :root {
    --ink: #37282F;
    --pink: #ED1D85;
    --pink-soft: #F7C6DD;
    --green-soft: #EEF5E2;
    --paper: #FFFFFF;
  }
  html, body {
    margin: 0;
    padding: 0;
    overflow: hidden;
    background: var(--paper);
  }
  .card {
    position: relative;
    width: 1200px;
    height: 740px;
    background: var(--paper);
    overflow: hidden;
    font-family: "Work Sans", "Helvetica Neue", Arial, sans-serif;
    color: var(--ink);
  }
  .card__petals {
    position: absolute;
    top: 0;
    right: 0;
    width: 480px;
    height: 480px;
    background:
      radial-gradient(circle at 100% 0%,
        var(--green-soft) 0%,
        var(--green-soft) 18%,
        var(--pink) 34%,
        var(--pink-soft) 55%,
        rgba(247, 198, 221, 0) 72%);
  }
  .card__name {
    position: absolute;
    left: 60px;
    top: 240px;
    margin: 0;
    font-weight: 300;
    font-size: 88px;
    line-height: 1;
    letter-spacing: 0.2em;
    text-transform: uppercase;
  }
  .card__phone {
    position: absolute;
    left: 82px;
    top: 412px;
    margin: 0;
    font-weight: 300;
    font-size: 37px;
    line-height: 1;
    letter-spacing: 0.16em;
    text-transform: uppercase;
  }
  .card__links {
    position: absolute;
    left: 78px;
    top: 548px;
    margin: 0;
    padding: 0;
    list-style: none;
    font-weight: 300;
    font-size: 33px;
    line-height: 55px;
    letter-spacing: 0.12em;
    text-transform: uppercase;
  }
  .card__link--social {
    padding-left: 8px;
  }
</style>
</head>
<body>
  <main class="card">
    <div class="card__petals" role="img" aria-label="Decorative spray of pink and pale green leaf-shaped petals fanning from the top-right corner"></div>

    <h1 class="card__name">Teodric</h1>

    <p class="card__phone">Phone: 0417360825</p>

    <ul class="card__links">
      <li class="card__link card__link--web">www.corvanephotography-example.com.au</li>
      <li class="card__link card__link--social">www.social-example.com/corvanephotography</li>
    </ul>
  </main>
</body>
</html>
```